250g Macaroni Possums with their Lamb Buddies

I have an exciting new product that i would like to add to our tourism based range - see gumleaftrails.com
I have a box (140Lx40Wx160H) that we will place a clear bag of pasta shapes in to. I need Aussie cartoon graphics for the box that bring the 3 pasta shapes to life. The main character will be a koala along with 2 teddy bear shapes. The main front panel will have a cut out window so the buyers can see the product. The shape of the window is up to the the designer. I can supply a scan of the pasta shapes, our logo, Bluefinch Seal logo, back panel type, bar code number, die line of box etc.....

**The Koala is the one sitting down**:-)

Target Market(s)

International tourists visiting Australia - mainly Asian

Industry/Entity Type

Tourism

Requirements
Must have
• Cute Koala

```html
<!DOCTYPE html>
<html lang="en">
<head>
<meta charset="utf-8">
<title>Macaroni Possums with their Lamb Buddies – Box Panels</title>
<link rel="stylesheet" href="https://fonts.googleapis.com/css2?family=Luckiest+Guy&family=Open+Sans:wght@400;600&display=swap">
<style>
  :root {
    --bg: #ece8e1;
    --orange-light: #fbb52a;
    --orange: #f59a12;
    --orange-deep: #ee8404;
    --title-red: #d8201e;
    --white: #ffffff;
    --pasta-yellow: #e7d36a;
    --pasta-shadow: #c9b24a;
    --koala-grey: #9a9a98;
    --koala-light: #cfcfcb;
    --badge-green: #2f9a5a;
    --badge-dark: #1e1e1e;
  }
  * { margin: 0; padding: 0; box-sizing: border-box; }
  html, body { width: 1200px; height: 662px; overflow: hidden; background: var(--bg); }
  .canvas { position: relative; width: 1200px; height: 662px; }

  .panel {
    position: absolute;
    top: 51px;
    height: 560px;
    background: linear-gradient(160deg, var(--orange-light) 0%, var(--orange) 55%, var(--orange-deep) 100%);
    overflow: hidden;
  }
  .panel--side { left: 270px; width: 140px; }
  .panel--front { left: 440px; width: 490px; }

  .title {
    font-family: "Luckiest Guy", "Impact", sans-serif;
    color: var(--title-red);
    line-height: 0.95;
    letter-spacing: 1px;
  }
  .title__sub {
    font-family: "Luckiest Guy", "Impact", sans-serif;
    color: var(--title-red);
    letter-spacing: 0.5px;
  }

  /* Front panel */
  .front-title { position: absolute; left: 30px; top: 36px; font-size: 74px; text-align: center; width: 430px; }
  .front-sub { position: absolute; left: 36px; top: 196px; font-size: 22px; }

  .pasta-shapes {
    position: absolute; left: 34px; top: 232px; width: 190px; height: 54px;
    background: linear-gradient(90deg, var(--pasta-yellow), var(--pasta-shadow), var(--pasta-yellow));
    border-radius: 22px; opacity: 0.9;
  }
  .window { position: absolute; left: 0; top: 285px; width: 270px; height: 190px; }
  .koala-photo {
    position: absolute; right: 18px; bottom: 0; width: 220px; height: 330px;
    background: radial-gradient(ellipse at 45% 40%, var(--koala-light) 0%, var(--koala-grey) 70%, #7d7d7a 100%);
    border-radius: 110px 110px 24px 24px;
  }
  .net-weight {
    position: absolute; left: 28px; top: 490px;
    font-family: "Open Sans", Arial, sans-serif; font-weight: 600;
    font-size: 18px; color: var(--white);
  }
  .badge { position: absolute; top: 486px; }
  .badge--green { left: 110px; width: 44px; height: 28px; background: var(--badge-green); border-radius: 4px; }
  .badge--dark { left: 168px; width: 30px; height: 32px; background: var(--badge-dark); }

  /* Side panel */
  .side-title { position: absolute; left: 10px; top: 30px; width: 120px; font-size: 22px; text-align: center; }
  .side-sub { position: absolute; left: 10px; top: 82px; width: 120px; font-size: 11px; text-align: center; }
  .side-copy {
    position: absolute; left: 12px; top: 120px; width: 116px;
    font-family: "Open Sans", Arial, sans-serif; font-size: 9px; line-height: 1.45;
    color: var(--white);
  }
  .side-copy p + p { margin-top: 8px; }
</style>
</head>
<body>
<main class="canvas">
  <section class="panel panel--side" aria-label="Box side panel">
    <h2 class="title side-title">Macaroni Possums</h2>
    <p class="title__sub side-sub">with their Lamb Buddies</p>
    <div class="side-copy">
      <p>Shaped pasta made in Australia from durum wheat semolina. Cook in boiling salted water for eight to ten minutes, drain and serve with your favourite sauce. Store in a cool dry place.</p>
      <p>Ingredients: durum wheat semolina, water.</p>
    </div>
  </section>

  <section class="panel panel--front" aria-label="Box front panel">
    <h1 class="title front-title">Macaroni<br>Possums</h1>
    <p class="title__sub front-sub">with their Lamb Buddies</p>

    <div class="pasta-shapes" role="img" aria-label="Row of three pasta shape illustrations"></div>

    <svg class="window" viewBox="0 0 270 190" role="img" aria-label="Cut-out window showing the pasta shapes inside">
      <defs>
        <linearGradient id="pastaFill" x1="0" y1="0" x2="1" y2="1">
          <stop offset="0" stop-color="#eadb7a"/>
          <stop offset="1" stop-color="#c7b04a"/>
        </linearGradient>
      </defs>
      <path d="M0 30 C60 0 110 10 150 30 C190 50 230 40 270 10 L270 150 C220 185 170 170 120 155 C70 140 30 150 0 170 Z" fill="url(#pastaFill)"/>
    </svg>

    <div class="koala-photo" role="img" aria-label="Photograph of a koala with a baby on its back"></div>

    <p class="net-weight">250gr</p>
    <div class="badge badge--green" aria-hidden="true"></div>
    <div class="badge badge--dark" aria-hidden="true"></div>
  </section>
</main>
</body>
</html>
```